Veterinary company needs powerpoint design

Our veterinary company working with in vitro fertilization needs a professional power point design and business card design.
for the power point desing we would like frontpage, plain slides, table slides, figure slides etc.
the colours should be matching our logo in blue-ish: blue, purple, grey, turquoise
We like it minimalistic, elegant, serious but with a warm touch.

Target Market(s)

Academic,

Industry/Entity Type

Veterinary

Contact Information for Business Card

name, title, email, phone, website

Font styles to use
Sans Serif

Colors
0455a3
3277b5
85abd2
cfdeed
6b449b
886aae
b8a6cd
e4daeb
86cfc6

```html
<!DOCTYPE html>
<html lang="en">
<head>
<meta charset="utf-8">
<title>Norvale Embryo Vet – Presentation Slides</title>
<link href="https://fonts.googleapis.com/css2?family=Open+Sans:wght@300;400;600;700&display=swap" rel="stylesheet">
<style>
:root{
  --navy:#0b4a82;
  --blue:#0455a3;
  --mid:#3277b5;
  --light:#85abd2;
  --pale:#cfdeed;
  --grey-bg:#e3e3e5;
  --copy:#7a7a7a;
  --ink:#333;
  --table-head:#6f7073;
  --rule:#b9b9b9;
}
*{margin:0;padding:0;box-sizing:border-box}
html,body{width:1200px;height:977px;overflow:hidden}
body{background:linear-gradient(180deg,#e6e6e8,#dcdcde);font-family:"Open Sans",Arial,sans-serif;position:relative}
.slide{position:absolute;width:372px;height:209px;background:#fff;overflow:hidden;box-shadow:0 7px 12px rgba(0,0,0,.22)}
.col1{left:22.5px}.col2{left:414px}.col3{left:806px}
.row1{top:23.6px}.row2{top:260px}.row3{top:496px}.row4{top:733px}
.bar{position:absolute;left:0;bottom:0;width:100%;height:4px;background:linear-gradient(90deg,var(--navy) 79%,var(--light) 79%)}
.num{position:absolute;left:351px;top:8px;width:11px;height:11px;border-radius:50%;background:var(--navy);color:#fff;font-size:6px;font-weight:700;line-height:11px;text-align:center}
.title{position:absolute;font-weight:400;font-size:15px;line-height:1;letter-spacing:1.6px;color:var(--navy);white-space:nowrap}
.title.center{left:0;width:100%;text-align:center}
.sub{position:absolute;font-size:6px;font-weight:700;color:var(--ink);white-space:nowrap}
.copy{position:absolute;font-size:4.4px;line-height:7.6px;color:var(--copy)}
.copy.center{text-align:center}
.photo{position:absolute}
.brand{position:absolute;display:flex;align-items:center;gap:4px;color:var(--navy);font-weight:600;white-space:nowrap}
.brand .dot{border-radius:50%;background:var(--navy);flex:none}

/* cover */
.cover .photo{inset:0;background:linear-gradient(180deg,#dadcdf 0%,#cfc9c2 28%,#a88f7a 48%,#8a6a53 70%,#a98e74 90%,#c2ab92 100%)}
.cover .band{position:absolute;left:0;top:82px;width:100%;height:127px;background:rgba(70,62,60,.18)}
.cover .brand{left:0;width:100%;justify-content:center;top:34px;font-size:15px}
.cover .brand .dot{width:10px;height:10px}
.cover .headline{position:absolute;left:0;width:100%;top:92px;text-align:center;color:#fff;font-weight:700;font-size:16.5px;letter-spacing:3.2px}

/* agenda */
.agenda .item{position:absolute;width:120px}
.agenda .item .sub{position:static;display:block;margin-bottom:3px}
.agenda .item .copy{position:static}

/* welcome */
.welcome .photo{left:234px;top:0;width:111px;height:182px;background:linear-gradient(180deg,#6d7a3e 0%,#56612f 35%,#7b4a2c 55%,#8a6038 75%,#9a9a55 100%)}
.welcome .brand{left:96px;top:172px;font-size:7px}
.welcome .brand .dot{width:6px;height:6px}

/* about */
.about .photo{left:35px;top:0;width:114px;height:173px;background:linear-gradient(160deg,#b89a80 0%,#c8955a 40%,#b57a3e 70%,#8c6a4c 100%)}

/* team */
.member{position:absolute;top:62px;width:80px;text-align:center}
.member .face{display:block;margin:0 auto;width:68px;height:68px;border-radius:50%;background:linear-gradient(180deg,#8b9a6e 0%,#6e7a5a 45%,#3f4a55 72%,#2f3a46 100%)}
.member .name{margin-top:9px;font-size:6px;font-weight:700;color:var(--ink)}
.member .role{margin-top:8px;font-size:4.2px;line-height:5px;color:var(--copy)}

/* services */
.services .p1{left:149px;top:0;width:101px;height:68px;background:linear-gradient(135deg,#bfc3c7,#6e747b 50%,#2f5b8a 80%,#d8dadc)}
.services .p2{left:171px;top:68px;width:101px;height:67px;background:radial-gradient(circle at 50% 50%,#8d8d8d 0 14%,#c9c9c9 22%,#b5b5b5 60%,#9e9e9e)}
.services .p3{left:149px;top:135px;width:100px;height:68px;background:radial-gradient(circle at 40% 55%,#bfbfbf 0 12%,#9f9fa3 30%,#8c8c92 100%)}
.services .svc{position:absolute;width:84px}
.services .svc .sub{position:static;display:block;margin-bottom:2px}
.services .svc .copy{position:static;line-height:5px}

/* problem / solution */
.solution-box{position:absolute;left:185px;top:0;width:163px;height:172px;background:var(--navy)}
.solution-box .title{color:#fff}
.solution-box .copy{color:#fff}

/* diagram */
.box{position:absolute;width:157px;height:59px;border:0.8px solid var(--navy)}
.box .head{height:10px;background:var(--navy);color:#fff;font-size:6px;font-weight:700;text-align:center;line-height:10px}
.box .copy{position:static;padding:5px 12px 0;text-align:center}

/* table */
.tbl{position:absolute;left:124px;top:71px;width:205px;height:113px}
.tbl-sub{position:absolute;left:37px;width:60px}
.tbl-sub .sub{position:static;display:block;margin-bottom:5px}
.tbl-sub .copy{position:static;line-height:4.4px}

/* bullets */
.bullet{position:absolute;left:28px;width:322px}
.bullet .ring{position:absolute;left:0;top:0;width:7.5px;height:7.5px;border-radius:50%;border:0.7px solid #888}
.bullet .sub{position:static;display:block;margin-left:12px;margin-bottom:3px}
.bullet .copy{position:static;margin-left:12px}
</style>
</head>
<body>

<!-- 1 Cover -->
<section class="slide col1 row1 cover">
  <div class="photo" role="img" aria-label="Photo of a woman and her dog sitting on a canyon rim"></div>
  <div class="band"></div>
  <div class="brand"><span class="dot"></span>Norvale Embryo Vet</div>
  <div class="headline">Business Presentation</div>
</section>

<!-- 2 Agenda -->
<section class="slide col1 row2 agenda">
  <h2 class="title" style="left:38px;top:25px">AGENDA</h2>
  <div class="item" style="left:37px;top:55px"><span class="sub">About Us</span><p class="copy">Short summary of this section and what the audience will learn here today.</p></div>
  <div class="item" style="left:218px;top:55px"><span class="sub">Our Works</span><p class="copy">Short summary of this section and what the audience will learn here today.</p></div>
  <div class="item" style="left:36px;top:103px"><span class="sub">Meet Our Team</span><p class="copy">Short summary of this section and what the audience will learn here today.</p></div>
  <div class="item" style="left:218px;top:103px"><span class="sub">The Problem</span><p class="copy">Short summary of this section and what the audience will learn here today.</p></div>
  <div class="item" style="left:37px;top:151px"><span class="sub">Our Services</span><p class="copy">Short summary of this section and what the audience will learn here today.</p></div>
  <div class="item" style="left:219px;top:151px"><span class="sub">The Solution</span><p class="copy">Short summary of this section and what the audience will learn here today.</p></div>
  <span class="num">2</span>
  <div class="bar"></div>
</section>

<!-- 3 Welcome -->
<section class="slide col1 row3 welcome">
  <h2 class="title" style="left:37px;top:25px">WELCOME MESSAGE</h2>
  <span class="sub" style="left:37px;top:55px">Subtitle</span>
  <p class="copy" style="left:37px;top:72px;width:170px">Our team supports breeders and clinics with careful embryo work, clear advice and steady follow up care. We combine research and practice to give every animal the best start. Our team supports breeders and clinics with careful embryo work, clear advice and steady follow up care. We combine research and practice to give every animal the best start.</p>
  <div class="brand"><span class="dot"></span>Norvale Embryo Vet</div>
  <div class="photo" role="img" aria-label="Photo of a brown horse standing in tall grass"></div>
  <span class="num">3</span>
  <div class="bar"></div>
</section>

<!-- 4 Full width text -->
<section class="slide col1 row4">
  <h2 class="title center" style="top:25px">A FULL WIDTH TEXT</h2>
  <p class="copy" style="left:37px;top:51px;width:297px">Our team supports breeders and clinics with careful embryo work, clear advice and steady follow up care. We combine research and practice to give every animal the best start. Our team supports breeders and clinics with careful embryo work, clear advice and steady follow up care. We combine research and practice to give every animal the best start.</p>
  <p class="copy" style="left:37px;top:105px;width:297px">Our team supports breeders and clinics with careful embryo work, clear advice and steady follow up care. We combine research and practice to give every animal the best start. Our team supports breeders and clinics with careful embryo work, clear advice and steady follow up care. We combine research and practice to give every animal the best start.</p>
  <span class="num">4</span>
  <div class="bar"></div>
</section>

<!-- 5 Two columns -->
<section class="slide col2 row1">
  <h2 class="title center" style="top:25px">TWO COLUMNS TEXT</h2>
  <p class="copy" style="left:45px;top:55px;width:130px">Our team supports breeders and clinics with careful embryo work, clear advice and steady follow up care. We combine research and practice to give every animal the best start. Our team supports breeders and clinics with careful embryo work, clear advice and steady follow up care. We combine research and practice to give every animal the best start.</p>
  <p class="copy" style="left:198px;top:55px;width:130px">Our team supports breeders and clinics with careful embryo work, clear advice and steady follow up care. We combine research and practice to give every animal the best start. Our team supports breeders and clinics with careful embryo work, clear advice and steady follow up care.</p>
  <span class="num">5</span>
  <div class="bar"></div>
</section>

<!-- 6 About us -->
<section class="slide col2 row2 about">
  <div class="photo" role="img" aria-label="Photo of a golden retriever balancing a treat on its nose"></div>
  <h2 class="title" style="left:168px;top:25px">ABOUT US</h2>
  <span class="sub" style="left:168px;top:55px">Subtitle</span>
  <p class="copy" style="left:168px;top:73px;width:171px">Our team supports breeders and clinics with careful embryo work, clear advice and steady follow up care. We combine research and practice to give every animal the best start. Our team supports breeders and clinics with careful embryo work, clear advice and steady follow up care. We combine research and practice to give every animal the best start.</p>
  <span class="num">6</span>
  <div class="bar"></div>
</section>

<!-- 7 Team -->
<section class="slide col2 row3">
  <h2 class="title center" style="top:25px">MEET OUR TEAM</h2>
  <div class="member" style="left:25px"><span class="face" role="img" aria-label="Portrait photo of Maren Holst"></span><p class="name">Maren Holst</p><p class="role">Veterinarian, certAVP equine<br>stud medicine</p></div>
  <div class="member" style="left:105px"><span class="face" role="img" aria-label="Portrait photo of Ida Kjeldsen"></span><p class="name">Ida Kjeldsen</p><p class="role">Veterinarian, PhD</p></div>
  <div class="member" style="left:185px"><span class="face" role="img" aria-label="Portrait photo of Tomás Varela"></span><p class="name">Tomás Varela</p><p class="role">Veterinarian, PhD Scholar</p></div>
  <div class="member" style="left:266px"><span class="face" role="img" aria-label="Portrait photo of Sofie Lind"></span><p class="name">Sofie Lind</p><p class="role">Veterinarian, PhD</p></div>
  <span class="num">7</span>
  <div class="bar"></div>
</section>

<!-- 8 Services -->
<section class="slide col2 row4 services">
  <h2 class="title" style="left:19px;top:25px">OUR SERVICES</h2>
  <span class="sub" style="left:19px;top:57px">Subtitle</span>
  <p class="copy" style="left:19px;top:74px;width:95px">Our team supports breeders and clinics with careful embryo work, clear advice and steady follow up care. We combine research and practice to give every animal the best start. Our team supports breeders and clinics with careful embryo work, clear advice and steady follow up care.</p>
  <div class="photo p1" role="img" aria-label="Photo of veterinarians working at a lab bench"></div>
  <div class="photo p2" role="img" aria-label="Microscope photo of an oocyte held by a pipette"></div>
  <div class="photo p3" role="img" aria-label="Microscope photo of an embryo with a micro needle"></div>
  <div class="svc" style="left:261px;top:23px"><span class="sub">Subtitle</span><p class="copy">Our team supports breeders and clinics with careful embryo work, clear advice and steady follow up care.</p></div>
  <div class="svc" style="left:284px;top:87px"><span class="sub">Subtitle</span><p class="copy">Our team supports breeders and clinics with careful embryo work, clear advice and steady follow up care.</p></div>
  <div class="svc" style="left:261px;top:160px"><span class="sub">Subtitle</span><p class="copy">Our team supports breeders and clinics with careful embryo work, clear advice and steady follow up care.</p></div>
  <span class="num">8</span>
  <div class="bar"></div>
</section>

<!-- 9 Problem / Solution -->
<section class="slide col3 row1">
  <h2 class="title" style="left:37px;top:43px">THE PROBLEM</h2>
  <span class="sub" style="left:37px;top:69px">Subtitle</span>
  <p class="copy" style="left:37px;top:84px;width:126px">Our team supports breeders and clinics with careful embryo work, clear advice and steady follow up care. We combine research and practice to give every animal the best start. Our team supports breeders and clinics with careful embryo work, clear advice and steady follow up care. We combine research and practice to give every animal the best start.</p>
  <div class="solution-box">
    <h2 class="title" style="left:19px;top:26px">THE SOLUTION</h2>
    <p class="copy" style="left:19px;top:49px;width:123px">Our team supports breeders and clinics with careful embryo work, clear advice and steady follow up care. We combine research and practice to give every animal the best start.</p>
    <p class="copy" style="left:19px;top:106px;width:123px">Our team supports breeders and clinics with careful embryo work, clear advice and steady follow up care. We combine research and practice to give every animal the best start.</p>
  </div>
  <span class="num">9</span>
  <div class="bar"></div>
</section>

<!-- 10 Diagram -->
<section class="slide col3 row2">
  <h2 class="title center" style="top:17px">DIAGRAM SECTION</h2>
  <p class="copy center" style="left:73px;top:37px;width:226px">Our team supports breeders and clinics with careful embryo work, clear advice and steady follow up care. We combine research and practice to give every animal the best start.</p>
  <div class="box" style="left:25px;top:64px"><div class="head">Subtitle</div><p class="copy">Our team supports breeders and clinics with careful embryo work, clear advice and steady follow up care. We combine research and practice to give every animal the best start.</p></div>
  <div class="box" style="left:194px;top:64px"><div class="head">Subtitle</div><p class="copy">Our team supports breeders and clinics with careful embryo work, clear advice and steady follow up care. We combine research and practice to give every animal the best start.</p></div>
  <div class="box" style="left:25px;top:130px"><div class="head">Subtitle</div><p class="copy">Our team supports breeders and clinics with careful embryo work, clear advice and steady follow up care. We combine research and practice to give every animal the best start.</p></div>
  <div class="box" style="left:194px;top:129px"><div class="head">Subtitle</div><p class="copy">Our team supports breeders and clinics with careful embryo work, clear advice and steady follow up care. We combine research and practice to give every animal the best start.</p></div>
  <span class="num">10</span>
  <div class="bar"></div>
</section>

<!-- 11 Table -->
<section class="slide col3 row3">
  <h2 class="title center" style="top:17px">TABLE+DISCRIPTION</h2>
  <p class="copy center" style="left:73px;top:37px;width:226px">Our team supports breeders and clinics with careful embryo work, clear advice and steady follow up care. We combine research and practice to give every animal the best start.</p>
  <div class="tbl-sub" style="top:65px"><span class="sub">Subtitle A</span><p class="copy">Short summary of this section and what the audience will learn here today.</p></div>
  <div class="tbl-sub" style="top:108px"><span class="sub">Subtitle B</span><p class="copy">Short summary of this section and what the audience will learn here today.</p></div>
  <div class="tbl-sub" style="top:151px"><span class="sub">Subtitle C</span><p class="copy">Short summary of this section and what the audience will learn here today.</p></div>
  <svg class="tbl" viewBox="0 0 205 113" width="205" height="113" aria-label="Five column data table">
    <rect x="0" y="0" width="205" height="11" fill="var(--table-head)"/>
    <g fill="#fff" font-family="Open Sans, sans-serif" font-size="5.6" font-weight="700" text-anchor="middle">
      <text x="20.5" y="8">ONE</text><text x="61.5" y="8">TWO</text><text x="102.5" y="8">THREE</text><text x="143.5" y="8">FOUR</text><text x="184.5" y="8">FIVE</text>
    </g>
    <g stroke="var(--rule)" stroke-width="0.6" fill="none">
      <rect x="0.3" y="11" width="204.4" height="101.7"/>
      <line x1="0" y1="23.7" x2="205" y2="23.7"/><line x1="0" y1="36.4" x2="205" y2="36.4"/>
      <line x1="0" y1="49.1" x2="205" y2="49.1"/><line x1="0" y1="61.8" x2="205" y2="61.8"/>
      <line x1="0" y1="74.5" x2="205" y2="74.5"/><line x1="0" y1="87.2" x2="205" y2="87.2"/>
      <line x1="0" y1="99.9" x2="205" y2="99.9"/>
      <line x1="41" y1="11" x2="41" y2="113"/><line x1="82" y1="11" x2="82" y2="113"/>
      <line x1="123" y1="11" x2="123" y2="113"/><line x1="164" y1="11" x2="164" y2="113"/>
    </g>
    <rect x="41" y="37" width="123" height="37" fill="var(--navy)"/>
    <text x="102.5" y="57.5" fill="#fff" font-family="Open Sans, sans-serif" font-size="5.6" font-weight="700" text-anchor="middle">DETAILS HERE</text>
  </svg>
  <span class="num">11</span>
  <div class="bar"></div>
</section>

<!-- 12 Bulleted list -->
<section class="slide col3 row4">
  <h2 class="title center" style="top:17px">BULLETED LIST TEXT</h2>
  <p class="copy center" style="left:73px;top:37px;width:226px">Our team supports breeders and clinics with careful embryo work, clear advice and steady follow up care. We combine research and practice to give every animal the best start.</p>
  <div class="bullet" style="top:70px"><span class="ring"></span><span class="sub">Your Title Here</span><p class="copy">Our team supports breeders and clinics with careful embryo work, clear advice and steady follow up care. We combine research and practice to give every animal the best start. Our team supports breeders and clinics with careful embryo work, clear advice and steady follow up care.</p></div>
  <div class="bullet" style="top:111px"><span class="ring"></span><span class="sub">Your Title Here</span><p class="copy">Our team supports breeders and clinics with careful embryo work, clear advice and steady follow up care. We combine research and practice to give every animal the best start. Our team supports breeders and clinics with careful embryo work, clear advice and steady follow up care.</p></div>
  <div class="bullet" style="top:151px"><span class="ring"></span><span class="sub">Your Title Here</span><p class="copy">Our team supports breeders and clinics with careful embryo work, clear advice and steady follow up care. We combine research and practice to give every animal the best start. Our team supports breeders and clinics with careful embryo work, clear advice and steady follow up care.</p></div>
  <span class="num">12</span>
  <div class="bar"></div>
</section>

</body>
</html>
```